Sponsorship and registration document for Charity Golf Day 2022

The project requires 2 documents to be updated to look more graphically savvy and professionally presentable.
1. Charity golf day sponsorship document
2. One page registration document.
The text has been completed. Text not to be changed - just graphics.
New images would be preferred.
The logos have been provided.

Target Market(s)

Corporate Sponsors and Golf players

Requirements
Must have
• Golf Theme

```html
<!DOCTYPE html>
<html lang="en">
<head>
<meta charset="utf-8">
<title>Charity Golf Day – Sponsorship Proposal</title>
<link href="https://fonts.googleapis.com/css2?family=Montserrat:wght@500;600;700;800&family=Arimo:ital,wght@0,400;0,700;1,700&display=swap" rel="stylesheet">
<style>
:root{
  --backdrop:#a6c47f;
  --navy:#1f3b8f;
  --navy-deep:#17307a;
  --green:#6cb33f;
  --green-light:#eef7e4;
  --field:#e3e3e3;
  --ink:#333;
  --muted:#666;
  --white:#fff;
}
*{box-sizing:border-box;margin:0;padding:0}
html,body{width:1200px;height:3000px;overflow:hidden;background:var(--backdrop)}
body{position:relative;font-family:"Arimo",Arial,sans-serif;color:var(--ink)}
.page{position:absolute;width:402px;height:568px;background:var(--white);overflow:hidden;font-size:6.4px;line-height:1.35}
.page.tint{background:var(--green-light)}
.page-head{position:absolute;top:22px;left:26px;right:26px;display:flex;align-items:center;gap:6px;font-size:5.4px;color:#444;text-transform:uppercase}
.page-head .rule{flex:1;height:1px;background:#bbb}
.grass{position:absolute;left:0;right:0;bottom:0;height:78px;background:linear-gradient(to bottom,rgba(255,255,255,0),#b9d98f 45%,#6f9a3c 80%,#4c7228)}
.web{position:absolute;bottom:12px;right:26px;font-family:"Montserrat",sans-serif;font-size:7px;letter-spacing:4.5px;color:#2a3a20;font-weight:600}
.content{position:absolute;top:42px;left:28px;right:28px}
h2{font-family:"Montserrat",sans-serif;font-weight:700;font-size:12.5px;color:var(--navy);line-height:1.2}
h2 .hl,.hl{color:var(--green)}
h2.bar{border-left:3px solid var(--navy);padding-left:6px}
h3{font-family:"Montserrat",sans-serif;font-weight:700;font-size:9.5px;color:var(--navy);margin:10px 0 6px}
p{margin-bottom:5px}
.lead{border-left:3px solid var(--navy);padding-left:7px;font-family:"Montserrat",sans-serif;font-weight:700;font-size:9px;color:var(--navy);line-height:1.3;margin-bottom:14px}
.checks{list-style:none}
.checks li{position:relative;padding-left:18px;margin-bottom:7px}
.checks li::before{content:"✓";position:absolute;left:0;top:-1px;width:7px;height:7px;border:1px solid var(--navy);font-size:6px;line-height:6px;text-align:center;color:var(--green);font-weight:700}
.rings{list-style:none;position:relative}
.rings li{position:relative;padding-left:18px;margin-bottom:4.5px}
.rings li::before{content:"";position:absolute;left:1px;top:0;width:5px;height:5px;border:1.5px solid var(--green);border-radius:50%;background:var(--white)}
.rings::before{content:"";position:absolute;left:4px;top:2px;bottom:4px;width:1px;background:var(--green)}
.rings.right li{padding-left:0;padding-right:18px;text-align:right}
.rings.right li::before{left:auto;right:1px}
.rings.right::before{left:auto;right:4px}
.tier{display:flex;align-items:center;height:24px;width:140px;background:linear-gradient(to right,var(--green),rgba(108,179,63,0));color:var(--white);font-family:"Montserrat",sans-serif;font-weight:700;font-size:11px;border-radius:12px 0 0 12px;margin-bottom:8px}
.tier .coin{width:24px;height:24px;border-radius:50%;background:var(--navy);color:var(--white);display:flex;align-items:center;justify-content:center;font-size:14px;margin-right:6px;border:2px solid var(--white)}
.tier.rev{margin-left:auto;background:linear-gradient(to left,var(--green),rgba(108,179,63,0));border-radius:0 12px 12px 0;justify-content:flex-end}
.tier.rev .coin{margin:0 0 0 6px;order:2}
.form-row{display:flex;align-items:center;margin-bottom:7px;font-weight:700;font-size:6.4px}
.form-row .lab{width:68px}
.form-row .box{flex:1;height:8px;background:var(--field)}
.player{color:var(--navy);font-weight:700}
/* cover */
.cover{left:375px;top:14px;height:569px;width:403px}
.cover-title{position:absolute;left:24px;top:26px;font-family:"Montserrat",sans-serif;font-weight:800;color:var(--navy);font-size:20px;line-height:1}
.cover-title .sub{display:block;color:var(--green);font-weight:600;font-size:15.5px;margin-top:3px}
.cover-tag{position:absolute;left:24px;top:84px;border-left:3px solid var(--navy);padding-left:6px;font-family:"Montserrat",sans-serif;font-weight:600;font-size:12px;line-height:1.15;color:var(--navy)}
.brand{position:absolute;right:26px;top:36px;display:flex;align-items:center;gap:5px;font-family:"Montserrat",sans-serif;font-weight:700;font-size:11px;color:var(--navy);line-height:1.1;text-align:right}
.brand .dot{width:22px;height:22px;border-radius:50%;background:#f2a22c}
.cover-photo{position:absolute;left:0;right:0;top:96px;height:300px}
.cover-msg{position:absolute;left:24px;top:402px;font-family:"Montserrat",sans-serif;font-weight:600;font-size:10px;line-height:1.4;color:#3a3a3a}
.date-box{position:absolute;left:24px;top:458px;border:2px solid var(--navy);padding:4px 8px;font-family:"Montserrat",sans-serif;color:var(--navy)}
.date-box .d{font-size:17px;letter-spacing:4px;font-weight:500}
.date-box .v{font-size:13px;letter-spacing:7px;border-top:1.5px solid var(--navy);margin-top:3px;padding-top:3px}
.cover-web{position:absolute;left:24px;top:540px;font-size:7.5px;letter-spacing:2.5px;color:#444}
/* letter */
.format{background:#ececec;margin:10px 0 14px;padding:10px 6px;display:flex;height:90px}
.format div{flex:1;text-align:center;font-weight:700;font-size:6px;padding:0 4px;border-left:1px solid #999}
.format div:first-child{border-left:none}
.format svg{display:block;margin:0 auto 6px}
.sig{display:inline-block;background:#ddd;padding:4px 6px;letter-spacing:3px;font-weight:700;margin:6px 0 8px}
/* why */
.blue-band{position:absolute;left:0;right:0;top:152px;height:122px;background:linear-gradient(to bottom,#1c3f9b,#274fb8 60%,#eaf0fa);padding:12px 28px;color:var(--white)}
.blue-band h2{color:var(--white);border-left-color:var(--green)}
.blue-band .rings::before{display:none}
.blue-band .rings li{margin-bottom:6px}
.blue-band .rings li::before{border-color:var(--green);background:var(--green);box-shadow:0 0 0 1.5px var(--navy) inset}
.amounts{display:flex;gap:14px;margin:10px 0}
.amounts div{flex:1;font-size:5.4px;font-weight:700;color:#444}
.amounts .pill{display:flex;align-items:center;height:15px;background:linear-gradient(to right,var(--green),rgba(108,179,63,0.2));border-radius:8px;color:var(--white);font-size:8px;margin-bottom:5px;width:80px}
.amounts .pill b{width:15px;height:15px;border-radius:50%;background:var(--navy);display:flex;align-items:center;justify-content:center;margin-right:4px}
/* day */
.meals{display:flex;background:#ececec;margin:10px 0 12px;padding:6px 4px}
.meals>div{flex:1;padding:0 6px}
.meals>div+div{border-left:2px solid var(--navy)}
.meals h4{font-family:"Montserrat",sans-serif;color:var(--navy);font-size:8px;margin-bottom:6px}
.meals p{display:flex;align-items:center;gap:8px;font-size:6px}
.meals span.ic{width:10px;height:10px;border-radius:3px;background:var(--green)}
.sched{display:flex;justify-content:space-between;margin-top:8px}
.sched div{width:50px;height:78px;border-radius:25px 25px 4px 4px;box-shadow:0 1px 3px rgba(0,0,0,.2);text-align:center;background:var(--white)}
.sched .t{width:46px;height:46px;margin:2px auto 5px;border-radius:50%;border:4px solid var(--green);display:flex;align-items:center;justify-content:center;font-weight:700;font-size:7px;color:var(--navy)}
.sched small{font-size:5.2px;color:var(--navy);font-weight:700;display:block;line-height:1.2}
/* pay */
.pay{display:grid;grid-template-columns:96px 1fr;row-gap:3px;font-size:6.2px}
.pay b{font-weight:700}
.pay .gap{grid-column:1/3;height:6px}
.card-line{display:flex;align-items:center;gap:6px;font-weight:700;margin:9px 0}
.card-line i{display:inline-block;width:14px;height:8px;background:var(--navy)}
/* contents page */
.contents{background:linear-gradient(to bottom,#f4f6fb 0%,#e3e9f4 45%,#5a78b8 80%,#28468f 100%)}
.contents-word{position:absolute;left:18px;top:258px;transform:rotate(-90deg);transform-origin:left top;font-family:"Montserrat",sans-serif;font-weight:800;font-size:40px;color:var(--navy)}
.toc{position:absolute;left:76px;top:64px;list-style:none;font-family:"Montserrat",sans-serif;font-weight:600;font-size:7.5px;color:#2b3e78}
.toc li{display:flex;align-items:center;gap:10px;margin-bottom:18.5px}
.toc b{width:17px;height:17px;border-radius:50%;background:var(--white);box-shadow:0 0 2px rgba(0,0,0,.3);display:flex;align-items:center;justify-content:center;font-size:9px}
.contact-h{position:absolute;left:28px;top:282px;font-family:"Montserrat",sans-serif;font-weight:700;font-size:17px;color:var(--navy)}
.contact-h::after{content:"";display:block;width:22px;height:2px;background:var(--navy);margin-top:4px}
.person{position:absolute;left:28px;display:flex;gap:28px;color:var(--white);font-size:6px}
.person .photo{width:52px;height:62px;background:#f2f2f2}
.person h5{font-family:"Montserrat",sans-serif;font-size:8px;font-weight:700}
.person .role{font-weight:700;font-size:6.5px;margin-bottom:6px}
.person .line{display:flex;gap:6px;align-items:center;margin-bottom:4px}
.person .phone{font-family:"Montserrat",sans-serif;font-size:9px;font-weight:700}
</style>
</head>
<body>

<!-- COVER -->
<section class="page cover">
  <h1 class="cover-title">CHARITY GOLF DAY<span class="sub">SPONSORSHIP PROPOSAL</span></h1>
  <div class="brand">Fairway<br>Service Club<span class="dot"></span></div>
  <p class="cover-tag">SUPPORTING PROSTATE<br><span class="hl">CANCER</span> RESEARCH</p>
  <div class="cover-photo">
    <svg width="403" height="300" viewBox="0 0 403 300" preserveAspectRatio="none" aria-hidden="true">
      <defs>
        <radialGradient id="sun" cx="0.6" cy="0.3" r="0.8">
          <stop offset="0" stop-color="#f6fbc4"/><stop offset="0.5" stop-color="#b9df55"/><stop offset="1" stop-color="#4f9a22"/>
        </radialGradient>
      </defs>
      <path d="M0 40 C120 0 260 60 403 10 L403 270 C300 300 150 240 0 280 Z" fill="url(#sun)"/>
      <path d="M0 40 C120 0 260 60 403 10 L403 0 C260 45 120 -10 0 28 Z" fill="var(--green)"/>
      <path d="M0 280 C150 240 300 300 403 266 L403 282 C300 310 150 256 0 292 Z" fill="var(--navy)"/>
    </svg>
    <div role="img" aria-label="Golf ball beside an iron on green grass with a putting golfer silhouette" style="position:absolute;inset:0"></div>
  </div>
  <p class="cover-msg">Help us hit prostate cancer<br>off the green and beat the most<br>common cancer in Australian men.</p>
  <div class="date-box"><div class="d">25<sup style="font-size:8px">TH</sup> MARCH, 2022</div><div class="v">ELMWOOD GOLF CLUB</div></div>
  <p class="cover-web">www.fsce.org.au/golf-day</p>
</section>

<!-- PAGE 2 : LETTER -->
<section class="page" style="left:163px;top:608px">
  <div class="page-head">Charity Golf Day<span class="rule"></span>Sponsorship Proposal</div>
  <div class="content">
    <p class="lead">Join us for an exclusive day on the private <span class="hl">ELMWOOD GOLF COURSE</span>, with all proceeds going to support Prostate Cancer Research, Awareness and Support.</p>
    <p>The Fairway Service Club of Eastfield will again be holding its Charity Golf Day with all proceeds used to support the Prostate Cancer Research, awareness and Support Programs. The venue will be the prestigious Elmwood Golf Club on Friday 25 March 2022, with a shotgun start at 8:00 am.</p>
    <p>We have enclosed for your information a copy of our promotional sponsor packages that outline the event, sponsorship package options and inclusions.</p>
    <h3>The format of the day involves:</h3>
    <div class="format">
      <div><svg width="22" height="24" viewBox="0 0 22 24" aria-hidden="true"><rect x="3" y="2" width="16" height="20" rx="2" fill="none" stroke="#6cb33f" stroke-width="2"/><path d="M7 8h8M7 12h8M7 16h6" stroke="#6cb33f" stroke-width="1.6"/></svg>Player registration, refreshments and light breakfast from 7:00am</div>
      <div><svg width="24" height="24" viewBox="0 0 24 24" aria-hidden="true"><circle cx="12" cy="13" r="9" fill="none" stroke="#6cb33f" stroke-width="2"/><path d="M12 13V8M10 2h4" stroke="#6cb33f" stroke-width="2"/></svg>Ambrose competition starting at 8:00am</div>
      <div><svg width="28" height="24" viewBox="0 0 28 24" aria-hidden="true"><circle cx="14" cy="12" r="8" fill="none" stroke="#6cb33f" stroke-width="2"/><path d="M3 3v18M25 3v18" stroke="#6cb33f" stroke-width="2"/></svg>Two Course lunch and presentations in the club house from 12:30pm</div>
    </div>
    <p>Your commitment to supporting health programs in our community is truly appreciated. With assistance from sponsors such as yourself, we will continue to see improvements in the support and treatment for men and their families with prostate cancer.</p>
    <p>We hope that you will consider supporting the worthwhile event that is open to any organisation or individual who wishes to enjoy the benefits of playing golf at the prestigious Elmwood Golf Club.</p>
    <p style="border-left:3px solid var(--navy);padding-left:7px;margin:12px 0 14px;font-size:7px">For more information, please check the website <b style="color:var(--navy)">(www.fsce.org.au/golf-day)</b> or should you wish to discuss any aspect of the event, please contact me on <b style="color:var(--navy)">0400 555 218.</b></p>
    <p style="font-size:7px">Your Sincerely,</p>
    <span class="sig">SIGNATURE</span>
    <p style="color:var(--navy);font-weight:700;margin-bottom:2px">HELENA MARSH</p>
    <p style="font-size:5.4px;line-height:1.8">Convener<br>Co - President 2021 -2022<br>Secretary 2021 - 2022<br>Fairway Service Club of Eastfield</p>
  </div>
  <div class="grass" role="img" aria-label="Close-up of green grass"></div>
  <span class="web">www.fsce.org.au</span>
</section>

<!-- PAGE 3 : WHY -->
<section class="page" style="left:619px;top:612px">
  <div class="page-head">Charity Golf Day<span class="rule"></span>Sponsorship Proposal</div>
  <div class="content">
    <h2 class="bar" style="margin-bottom:8px">Why Prostate Cancer?</h2>
    <ul class="checks">
      <li>Prostate cancer is the most diagnosed cancer in Australian men.</li>
      <li>Approximately 20,000 Australian men are diagnosed with prostate cancer each year.</li>
      <li>Over 200,000 Australian men are living with a diagnosis prostate cancer.</li>
      <li>95% of Australian men diagnosed with prtostate cancer survive for at least 5 years.</li>
      <li>Almost 3,500 Australian men die of prostate cancer each year.</li>
    </ul>
  </div>
  <div class="blue-band">
    <h2 class="bar" style="margin-bottom:9px">Why are we asking <span class="hl">you to be involved?</span></h2>
    <ul class="rings">
      <li>Every day 54 Australian men will be told they have prostate cancer</li>
      <li>70% of research applications are unfunded</li>
      <li>1 in 6 men will suffer from prostate cancer</li>
      <li>9 families lose a loved one to prostate cancer every day</li>
      <li>Only 1 in 3 men have access to a specialist nurse</li>
    </ul>
  </div>
  <div class="content" style="top:284px">
    <h2 class="bar">What this fundraising <span class="hl">event can achieve</span></h2>
    <div class="amounts">
      <div><span class="pill"><b>$</b>12,500</span>Could provide funding for a researcher working for one month on a project to reduce side – effects post treatment.</div>
      <div><span class="pill"><b>$</b>30,000</span>Could provide funding for a senior scientist for three months working on a project to improve treatments for prostate cancer that has spread to the bones.</div>
      <div><span class="pill"><b>$</b>50,000</span>Could fund a project to improve early – diagnosis for men with a family history of prostate cancer.</div>
    </div>
    <p>Proceeds from this event will be donated to Prostate Cancer Research Group at the Southbank University Health Research Institute, to fund world leading, innovative research and to support men and their families affected by prostate cancer.</p>
    <p>Their innovative research program has a strong translational approach, involving lab-based studies with tissues donated by patients with prostate cancer. Their collaborative studies with clinicians and patient advocates address questions that are relevant to patient care. The findings have the potential to improve the management and outcomes of men with different stages of prostate cancer. Recent studies have informed international guidelines for diagnosis of prostate cancer and led to new clinical trials.</p>
    <p style="font-weight:700;margin-top:8px">For more information visit their website<br>www.southbank.example.edu/health-institute/prostate-research</p>
  </div>
  <div class="grass" role="img" aria-label="Close-up of green grass"></div>
  <span class="web">www.fsce.org.au</span>
</section>

<!-- PAGE 4 : THE DAY -->
<section class="page" style="left:163px;top:1196px">
  <div class="page-head">Charity Golf Day<span class="rule"></span>Sponsorship Proposal</div>
  <div class="content">
    <h2>Friday 25 March 2022 at Elmwood Golf Club</h2>
    <p style="margin-top:6px">The Championship Par 72 layout of 6179 metres is a genuine test to all standards of players. Situated only 15 minutes from the city, the course meanders along the Yarra River providing a beautiful vista and is home for 100's of species of native birds and tall-established trees.</p>
    <div class="meals">
      <div><h4>Breakfast</h4><p><span class="ic"></span>Light Breakfast</p><p style="margin-top:8px"><span class="ic"></span>Tea and coffee</p></div>
      <div><h4>Lunch</h4><p><span class="ic"></span>Two-Course Lunch</p><p style="margin-top:8px"><span class="ic"></span>Drinks at Bar Prices</p></div>
    </div>
    <h2 class="bar" style="font-size:11px;margin-bottom:8px">What else to <span class="hl">expect:</span></h2>
    <ul class="checks">
      <li>4-person Ambrose</li>
      <li>On course competitions such as nearest the pins and longest drive</li>
      <li>Trophies &amp; Prizes</li>
      <li>On the day you will have access to practice putting, chipping greens, and driving range</li>
      <li>A refreshment cart will circulate the golf course for players to purchase refreshments at own cost</li>
      <li>Hire Equipment<br><span style="font-size:5.2px;line-height:1.6">• Hire sets (Standard) $35.00 per set; (Premium) $50.00 per set<br>• Hire shoes $10.00 per pair<br>• Carts $40.00 each (Booking essential as numbers are limited, but it is an easy course to walk)</span></li>
    </ul>
    <h2 class="bar" style="font-size:11px;margin-top:10px">Schedule:</h2>
    <div class="sched">
      <div><span class="t">7-7.30<br>am</span><small>Registration</small></div>
      <div><span class="t">7:15am</span><small>Breakfast</small></div>
      <div><span class="t">7:45am</span><small>Player<br>Briefing</small></div>
      <div><span class="t">8.00am</span><small>Shotgun<br>start</small></div>
      <div><span class="t">12.30pm</span><small>Lunch,<br>Presentation<br>/Prizes</small></div>
      <div><span class="t">3.00pm</span><small>Finish</small></div>
    </div>
  </div>
  <div class="grass" role="img" aria-label="Close-up of green grass"></div>
  <span class="web">www.fsce.org.au</span>
</section>

<!-- PAGE 5 : GOLD / SILVER -->
<section class="page" style="left:619px;top:1196px">
  <div class="page-head">Charity Golf Day<span class="rule"></span>Sponsorship Proposal</div>
  <div class="content">
    <h2 class="bar" style="margin-bottom:10px">Sponsorship <span class="hl">Opportunities</span></h2>
    <div class="tier"><span class="coin">$</span>GOLD $5000</div>
    <p style="font-weight:700;margin-bottom:8px">The Gold Sponsor is entitled to the following:</p>
    <ul class="rings">
      <li>Event naming rights</li>
      <li>Eight (8) representatives playing in the event, including all green fees, four (4) carts, light breakfast &amp; 2 course lunch</li>
      <li>Your company signage / banners displayed exclusively at club entrance and social area.</li>
      <li>Your logo and your company information on all promotional and marketing material being used on the day including our website, email to database and our social media channels.</li>
      <li>A Banner with company logo on the first hole</li>
      <li>Opportunity to say a few words at the beginning of the game as the chief sponsor of the event.</li>
      <li>Your company merchandise on display.</li>
      <li>Presenting the winners awards</li>
      <li>Free advertising in our Service Club Newsletter, website, and social media channels for 12 months.</li>
      <li>Opportunity to “capture” prospective clients on the day</li>
      <li>Great Publicity: Be seen as being associated with an excellent cause</li>
    </ul>
    <div class="tier rev" style="margin-top:10px"><span class="coin">$</span>SILVER $2500</div>
    <p style="font-weight:700;margin-bottom:8px;text-align:right">The Silver Sponsor is entitled to the following:</p>
    <ul class="rings right">
      <li>Four (4) representatives playing in the event, including all green fees, two (2) carts, light breakfast &amp; 2 course lunch</li>
      <li>Exclusive banner with your company logo on a tee of choice (except hole 1)</li>
      <li>Opportunity to say a few words as a major sponsor</li>
      <li>Your company merchandise on display.</li>
      <li>Your logo and your company information on all promotional and marketing material being used on the day including our website, email to database and our social media channels.</li>
      <li>Free advertising in our Service Club Newsletter, website, and social media channels for 6 months.</li>
      <li>Opportunity to “capture” prospective clients on the day</li>
      <li>Great Publicity: Be seen as being associated with an excellent cause</li>
    </ul>
  </div>
  <div class="grass" role="img" aria-label="Close-up of green grass"></div>
  <span class="web">www.fsce.org.au</span>
</section>

<!-- PAGE 6 : BRONZE / PAYMENT -->
<section class="page" style="left:163px;top:1796px;height:574px">
  <div class="page-head">Charity Golf Day<span class="rule"></span>Sponsorship Proposal</div>
  <div class="content">
    <div class="tier"><span class="coin">$</span>BRONZE $650</div>
    <p style="font-weight:700;margin-bottom:8px">This Bronze Sponsor is entitled to the following:</p>
    <ul class="rings">
      <li>Two (2) representatives playing in the event, including all green fees, light breakfast &amp; 2 course lunch</li>
      <li>Exclusive banner with your company logo on a tee</li>
      <li>Your logo and your company information on all promotional and marketing material being used on the day including our website, email to database and our social media channels.</li>
      <li>Great Publicity: Be seen as being associated with an excellent cause</li>
      <li>Opportunity to “capture” prospective clients on the day</li>
      <li>Company merchandising display</li>
      <li>Additional players - $150 per person (including all green fees, light breakfast &amp; 2-course lunch).</li>
    </ul>
    <h2 style="margin-top:10px">Additional Players - $150 per person</h2>
    <p style="font-weight:700;margin-top:3px">includes all green fees, light breakfast &amp; two (2) course lunch</p>
    <h2 class="bar" style="margin:14px 0 10px"><span class="hl">PAYMENT OPTIONS</span></h2>
    <div class="pay">
      <b>By Cheque:</b><span>Please make cheques payable to The Fairway Service Club of Eastfield<br>PO Box 000<br>Eastfield, Vic 3000</span>
      <span class="gap"></span>
      <b>By Direct Account Name:</b><span>Fairway Service Club of Eastfield</span>
      <b>Deposit: Bank:</b><span>Harbour Community Bank</span>
      <b>BSB:</b><span>000 000</span>
      <b>Account Number:</b><span>123 456 789</span>
      <b>Comment:</b><span>FSCGolfDay/your name</span>
    </div>
    <div class="card-line"><span style="width:144px">By Credit Card:</span>CREDIT <i></i><span style="width:40px"></span>DEBIT <i></i></div>
    <div class="form-row"><span class="lab" style="width:44px">Card No.</span><span class="box"></span><span style="margin:0 6px">Expiry:</span><span class="box" style="flex:0 0 24px"></span><span style="margin:0 2px">/</span><span class="box" style="flex:0 0 24px"></span></div>
    <div class="form-row" style="margin-top:10px"><span class="lab">Cardholder's Name:</span><span class="box"></span></div>
    <div class="form-row" style="margin-top:10px"><span class="lab">Cardholder's Signature:</span><span class="box"></span><span style="margin:0 6px">Date:</span><span class="box" style="flex:0 0 70px"></span></div>
  </div>
  <div class="grass" role="img" aria-label="Close-up of green grass"></div>
  <span class="web">www.fsce.org.au</span>
</section>

<!-- PAGE 7 : APPLICATION FORM -->
<section class="page tint" style="left:619px;top:1796px;height:574px">
  <div class="page-head">Charity Golf Day<span class="rule"></span>Application Form</div>
  <div class="content">
    <h2 class="bar" style="margin-bottom:16px">Sponsorship Package: <span class="hl">(Please Tick)</span></h2>
    <div style="display:flex;justify-content:space-between;font-weight:700;margin-bottom:14px">
      <span><i style="display:inline-block;width:9px;height:9px;background:#ccc;vertical-align:middle;margin-right:4px"></i>Gold ($5,000)</span>
      <span><i style="display:inline-block;width:9px;height:9px;background:#ccc;vertical-align:middle;margin-right:4px"></i>Silver ($2,500)</span>
      <span><i style="display:inline-block;width:9px;height:9px;background:#ccc;vertical-align:middle;margin-right:4px"></i>Bronze ($650)</span>
      <span><i style="display:inline-block;width:9px;height:9px;background:#ccc;vertical-align:top;margin-right:4px"></i>Additional<br>Players ($150)</span>
    </div>
    <div class="form-row"><span class="lab">Company:</span><span class="box"></span></div>
    <div class="form-row" style="margin-top:16px"><span class="lab">Address:</span><span class="box"></span></div>
    <div class="form-row" style="margin-top:16px"><span class="lab">Suburb:</span><span class="box"></span><span style="margin:0 6px">P/Code:</span><span class="box" style="flex:0 0 66px"></span></div>
    <div class="form-row"><span class="lab">Mobile:</span><span class="box"></span></div>
    <div class="form-row" style="margin-top:10px"><span class="lab">Contact Name:</span><span class="box"></span></div>
    <div class="form-row" style="margin-top:10px"><span class="lab">Contact Email:</span><span class="box"></span></div>
    <h2 class="bar" style="margin:14px 0 12px;font-size:11px">Team Name:</h2>
    <div class="form-row"><span class="lab player">PLAYER 1:</span><span class="box"></span></div>
    <div class="form-row"><span class="lab">Official GA H/Cap:</span><span class="box"></span></div>
    <div class="form-row" style="margin-top:24px"><span class="lab player">PLAYER 2:</span><span class="box"></span></div>
    <div class="form-row"><span class="lab">Official GA H/Cap:</span><span class="box"></span></div>
    <div class="form-row" style="margin-top:24px"><span class="lab player">PLAYER 3:</span><span class="box"></span></div>
    <div class="form-row"><span class="lab">Official GA H/Cap:</span><span class="box"></span></div>
    <div class="form-row" style="margin-top:24px"><span class="lab player">PLAYER 4:</span><span class="box"></span></div>
    <div class="form-row"><span class="lab">Official GA H/Cap:</span><span class="box"></span></div>
    <p style="margin-top:18px;color:var(--navy);font-style:italic;font-weight:700;font-size:6px">* Please Note: any player without an official GA H/Cap will be given a maximum handicap of 27 (Males) &amp; 36 (Females).</p>
  </div>
  <div class="grass" role="img" aria-label="Close-up of green grass"></div>
  <span class="web">www.fsce.org.au</span>
</section>

<!-- PAGE 8 : TEAM CONTINUED -->
<section class="page tint" style="left:163px;top:2402px;height:576px">
  <div class="page-head">Charity Golf Day<span class="rule"></span>Application Form</div>
  <div class="content">
    <h2 class="bar" style="margin-bottom:14px">Team Name:</h2>
    <div class="form-row"><span class="lab player">PLAYER 5:</span><span class="box"></span></div>
    <div class="form-row"><span class="lab">Official GA H/Cap:</span><span class="box"></span></div>
    <div class="form-row" style="margin-top:26px"><span class="lab player">PLAYER 6:</span><span class="box"></span></div>
    <div class="form-row"><span class="lab">Official GA H/Cap:</span><span class="box"></span></div>
    <div class="form-row" style="margin-top:26px"><span class="lab player">PLAYER 7:</span><span class="box"></span></div>
    <div class="form-row"><span class="lab">Official GA H/Cap:</span><span class="box"></span></div>
    <div class="form-row" style="margin-top:26px"><span class="lab player">PLAYER 8:</span><span class="box"></span></div>
    <div class="form-row"><span class="lab">Official GA H/Cap:</span><span class="box"></span></div>
    <p style="margin-top:14px;color:var(--navy);font-style:italic;font-weight:700;font-size:6px">* Please Note: any player without an official GA H/Cap will be given a maximum handicap of 27 (Males) &amp; 36 (Females).</p>
    <h2 class="bar" style="margin:26px 0 16px">Cancellation Terms</h2>
    <p style="font-weight:700;font-size:6.2px">If the organiser cancels the event prior to the scheduled date, the sponsor is entitled to a 100% refund. If the event is rescheduled by the organiser, and the player or sponsor can reasonably demonstrate their inability to participate they will be entitled to a full refund. In the event of a player or sponsor cancellation, the Service Club of Eastfield reserves the right to retain monies paid in full unless resold. Any cancellations must be advised in writing via email to the Convenor Helena Marsh (helena.marsh@mailbox.example).</p>
  </div>
  <div class="grass" role="img" aria-label="Close-up of green grass"></div>
  <span class="web">www.fsce.org.au</span>
</section>

<!-- PAGE 9 : CONTENTS / CONTACT -->
<section class="page contents" style="left:619px;top:2402px;height:576px" role="img" aria-label="Contents and contact page over a faint photo of a golfer on a course">
  <div class="page-head">Charity Golf Day<span class="rule"></span>Sponsorship Proposal</div>
  <div class="contents-word">Contents:</div>
  <ol class="toc">
    <li><b>2</b>CHARITY GOLF DAY INVITATION</li>
    <li><b>3</b>ABOUT PROSTATE CANCER</li>
    <li><b>3</b>WHY ARE WE ASKING YOU TO BE INVOLVED</li>
    <li><b>4</b>WHAT TO EXPECT</li>
    <li><b>5</b>SPONSORSHIP OPPORTUNITIES</li>
    <li><b>7</b>APPLICATION FORM</li>
  </ol>
  <h2 class="contact-h">CONTACT US</h2>
  <div class="person" style="top:322px">
    <div class="photo"></div>
    <div>
      <h5>HELENA MARSH</h5>
      <p class="role">CONVENOR<br><span style="font-size:5.6px">Co - President, Fairway Service Club</span></p>
      <p class="line"><svg width="8" height="8" viewBox="0 0 10 10" aria-hidden="true"><path d="M2 1l2 2-1 1.5c.8 1.5 1.5 2.2 3 3L7.5 6l2 2-1.5 1.5C4 9 1 6 .5 1.5z" fill="#fff"/></svg><span class="phone">0400 555 218</span></p>
      <p class="line"><svg width="8" height="8" viewBox="0 0 10 10" aria-hidden="true"><rect x="0.5" y="2" width="9" height="6" fill="none" stroke="#fff"/><path d="M.5 2l4.5 3.5L9.5 2" fill="none" stroke="#fff"/></svg>helena.marsh@mailbox.example</p>
      <p class="line"><svg width="8" height="8" viewBox="0 0 10 10" aria-hidden="true"><circle cx="5" cy="5" r="4.3" fill="none" stroke="#fff"/><path d="M.7 5h8.6M5 .7c-2 2.5-2 6 0 8.6M5 .7c2 2.5 2 6 0 8.6" fill="none" stroke="#fff" stroke-width=".7"/></svg>www.fsce.org.au/golf-day</p>
    </div>
  </div>
  <div class="person" style="top:420px">
    <div class="photo"></div>
    <div>
      <h5>CLARA BENTON</h5>
      <p class="role">EVENT MANAGER</p>
      <p class="line"><svg width="8" height="8" viewBox="0 0 10 10" aria-hidden="true"><rect x="0.5" y="2" width="9" height="6" fill="none" stroke="#fff"/><path d="M.5 2l4.5 3.5L9.5 2" fill="none" stroke="#fff"/></svg>clara.benton@mailbox.example</p>
    </div>
  </div>
  <span class="web" style="color:#fff">www.fsce.org.au</span>
</section>

</body>
</html>
```